Business Card and Stationary for Brantley Consulting
Brantley Consulting
Business Card and Stationary for Brantley Consulting - Energy
Creative Brief
Professional
Dale Pruitt
Inspector
17 Juniper Court Red Deer Alberta, Canada T4P 2K9
dale_pruitt@mailvora.com
brantleyconsulting brantleyconsulting
2 sided business card and stationary design. Let's see what you got.

```html
<!DOCTYPE html>
<html lang="en">
<head>
<meta charset="utf-8">
<title>Brantley Consulting – Business Card</title>
<link href="https://fonts.googleapis.com/css2?family=Exo+2:wght@400;600;800&display=swap" rel="stylesheet">
<style>
  :root{
    --stage:#6a6a6a;
    --card:#050607;
    --blue-deep:#0b3f8f;
    --blue:#1f7fe0;
    --blue-bright:#3fb4ff;
    --cyan:#5fe6f0;
    --ink:#ffffff;
    --ink-soft:#cfd6de;
  }
  html,body{margin:0;padding:0;overflow:hidden;}
  body{
    width:1200px;height:840px;background:var(--stage);
    font-family:"Exo 2",Arial,sans-serif;position:relative;
  }
  .card{
    position:absolute;width:500px;height:290px;background:var(--card);
    overflow:hidden;border-radius:3px;
    box-shadow:0 10px 30px rgba(0,0,0,.35);
  }
  .card--front{left:70px;top:275px;}
  .card--back{left:630px;top:275px;}
  .card svg.swoosh{position:absolute;inset:0;width:100%;height:100%;}
  .holder{position:absolute;right:28px;top:36px;text-align:right;color:var(--ink);}
  .holder__name{font-size:19px;font-weight:600;letter-spacing:1.5px;margin:0;}
  .holder__title{font-size:11px;letter-spacing:2px;margin:4px 0 0;color:var(--ink-soft);}
  .address{position:absolute;right:28px;top:108px;text-align:right;color:var(--ink-soft);
    font-size:10.5px;line-height:15px;margin:0;}
  .contacts{position:absolute;right:28px;top:170px;list-style:none;margin:0;padding:0;
    color:var(--ink-soft);font-size:10px;text-align:right;}
  .contacts li{display:flex;justify-content:flex-end;align-items:center;gap:7px;height:17px;}
  .contacts svg{width:9px;height:9px;fill:var(--ink-soft);}
  .brand{position:absolute;display:flex;align-items:center;gap:8px;color:var(--blue-bright);
    font-weight:800;letter-spacing:1px;text-transform:uppercase;line-height:1.05;}
  .brand__dot{border-radius:50%;background:var(--blue-bright);flex:none;}
  .card--front .brand{left:30px;top:200px;font-size:19px;}
  .card--front .brand__dot{width:14px;height:14px;}
  .card--back .brand{left:70px;top:118px;font-size:30px;}
  .card--back .brand__dot{width:22px;height:22px;}
</style>
</head>
<body>

<section class="card card--front" aria-label="Business card front">
  <svg class="swoosh" viewBox="0 0 500 290" preserveAspectRatio="none" aria-hidden="true">
    <defs>
      <linearGradient id="frontBlue" x1="0" y1="0" x2="1" y2="0.6">
        <stop offset="0" stop-color="#0b3f8f"/>
        <stop offset="0.35" stop-color="#1f7fe0"/>
        <stop offset="0.6" stop-color="#3fb4ff"/>
        <stop offset="1" stop-color="#0a2f6a"/>
      </linearGradient>
    </defs>
    <path d="M0 0 H330 C250 40 190 95 120 150 C80 180 40 215 0 230 Z" fill="url(#frontBlue)"/>
    <path d="M330 0 C250 40 190 95 120 150 C80 180 40 215 0 230" fill="none" stroke="#5fe6f0" stroke-width="2" opacity=".8"/>
    <path d="M360 0 C270 55 200 120 130 175 C90 205 45 235 0 250" fill="none" stroke="#1f7fe0" stroke-width="3"/>
    <path d="M380 0 C290 65 215 135 150 185" fill="none" stroke="#0b3f8f" stroke-width="2"/>
  </svg>
  <div class="holder">
    <p class="holder__name">DALE PRUITT</p>
    <p class="holder__title">DIRECTOR</p>
  </div>
  <p class="address">17 Juniper Court<br>Red Deer AB</p>
  <ul class="contacts">
    <li>403 555 0142 <svg viewBox="0 0 10 10"><path d="M2 0l2 2-1 1.5c.8 1.5 2 2.7 3.5 3.5L8 6l2 2-1.5 2C4 9.5.5 6 0 1.5Z"/></svg></li>
    <li>403 555 0142 <svg viewBox="0 0 10 10"><path d="M2.5 0h5a1 1 0 0 1 1 1v8a1 1 0 0 1-1 1h-5a1 1 0 0 1-1-1V1a1 1 0 0 1 1-1Zm0 1.5v6h5v-6Z"/></svg></li>
    <li>403 555 0142 <svg viewBox="0 0 10 10"><path d="M1 3h8v5H1Zm2-3h4v2.5H3Z"/></svg></li>
    <li>dale_pruitt@mailvora.com <svg viewBox="0 0 10 10"><path d="M0 2h10v6H0Zm1 1 4 3 4-3Z"/></svg></li>
    <li>www.brantleyconsulting.com <svg viewBox="0 0 10 10"><circle cx="5" cy="5" r="5"/></svg></li>
  </ul>
  <div class="brand"><span class="brand__dot"></span><span>Brantley<br>Consulting</span></div>
</section>

<section class="card card--back" aria-label="Business card back">
  <svg class="swoosh" viewBox="0 0 500 290" preserveAspectRatio="none" aria-hidden="true">
    <defs>
      <linearGradient id="backBlue" x1="0" y1="0" x2="1" y2="1">
        <stop offset="0" stop-color="#3fb4ff"/>
        <stop offset="0.5" stop-color="#1f7fe0"/>
        <stop offset="1" stop-color="#0b3f8f"/>
      </linearGradient>
    </defs>
    <path d="M300 0 H500 V290 H470 C480 190 430 80 300 0 Z" fill="url(#backBlue)" opacity=".35"/>
    <path d="M300 0 C430 80 480 190 470 290" fill="none" stroke="#3fb4ff" stroke-width="4"/>
    <path d="M340 0 C450 70 495 160 500 230" fill="none" stroke="#5fe6f0" stroke-width="2"/>
    <path d="M270 0 C400 95 445 200 430 290" fill="none" stroke="#1f7fe0" stroke-width="2"/>
  </svg>
  <div class="brand"><span class="brand__dot"></span><span>Brantley<br>Consulting</span></div>
</section>

</body>
</html>
```